Manual design

Hello,

I am looking for someone creative to help me design my Real Estate related manual. I am looking for something simple yet impressive. It would be designed around my logo and brand colors and I would also like it to have a local feel, perhaps with photos I could provide of my area/hometown. I am really shooting for an impressive company and branded look, while keeping it neat without too much going on.

I have the content that I would like to include, I am just struggling with the design of the manual in general.

I have attached a copy of my logo, my companys logo, and a publisher file of what I had previously done. Please do not think the design I previously used is something to work off of if you deem it better to use another feel. I am looking for originality, unless you can improve upon my old file. Any questions, please feel free to reach out to me.

The content in the provided brochure will remain the same, it is the design aspect I need help with. Thanks

Target Market(s)

My target market is home sellers aged 25-55, people usually selling their 1st or second home

Industry/Entity Type

Real Estate

Requirements
Must have
• -A simple to read design focused around my logo and colors
-A local sense
Should not have
• Drawings, only real photos

```html
<!DOCTYPE html>
<html lang="en">
<head>
<meta charset="utf-8">
<title>Seller Manual – Pages 4 and 5</title>
<link rel="stylesheet" href="https://fonts.googleapis.com/css2?family=Libre+Baskerville&family=EB+Garamond:ital@1&family=Jost:wght@400;500&display=swap">
<style>
  :root {
    --navy: #1f2647;
    --page-grey: #c6c7c9;
    --band-grey: #c9cacc;
    --power-grey: #8a8b8e;
    --bar-dark: #636366;
    --bar-light: #949598;
    --white: #ffffff;
    --ink: #1d1d22;
  }
  * { margin: 0; padding: 0; box-sizing: border-box; }
  html, body { width: 1200px; height: 900px; overflow: hidden; background: var(--white); }
  body { position: relative; font-family: "Jost", Arial, sans-serif; color: var(--navy); }

  .spread { position: absolute; left: 90px; top: 88px; width: 1020px; height: 722px; box-shadow: 0 0 6px rgba(0,0,0,.18); background: var(--white); }
  .page { position: absolute; top: 0; height: 722px; }
  .page--left { left: 0; width: 510px; background: var(--page-grey); }
  .page--right { left: 512px; width: 508px; background: var(--white); }

  .page-number { position: absolute; top: 20px; width: 24px; height: 18px; background: var(--navy); color: var(--white); font-size: 8px; line-height: 18px; text-align: center; }
  .page--left .page-number { left: 61px; }
  .page--right .page-number { left: 423px; }

  .page-title { position: absolute; font-family: "Libre Baskerville", Georgia, serif; font-weight: 400; font-size: 23px; line-height: 30px; color: var(--navy); letter-spacing: -0.2px; white-space: nowrap; }
  .page--left .page-title { left: 61px; top: 56px; }
  .page--right .page-title { left: 59px; top: 57px; }

  .lede { position: absolute; font-family: "EB Garamond", Georgia, serif; font-style: italic; font-size: 11.5px; color: #444; line-height: 18px; }
  .page--left .lede { left: 61px; top: 121px; white-space: nowrap; }
  .page--right .lede { left: 59px; top: 116px; width: 395px; }

  .question-list { position: absolute; left: 62px; top: 172px; width: 385px; list-style: none; }
  .question-list li { height: 34px; margin-bottom: 1.6px; background: var(--white); font-size: 9.3px; line-height: 34px; padding-left: 14px; color: var(--navy); white-space: nowrap; }

  .power-thought { position: absolute; left: 62px; top: 492px; width: 385px; height: 87px; background: var(--power-grey); padding: 13px 14px; color: var(--white); }
  .power-thought h3 { font-family: "Libre Baskerville", Georgia, serif; font-weight: 400; font-size: 15px; margin-bottom: 12px; }
  .power-thought p { font-size: 8.6px; line-height: 14px; text-transform: uppercase; }

  .section-band { position: absolute; left: 59px; width: 376px; height: 19px; background: var(--band-grey); font-family: "Libre Baskerville", Georgia, serif; font-weight: 400; font-size: 10.5px; line-height: 19px; padding-left: 6px; color: var(--navy); white-space: nowrap; }
  .copy { position: absolute; left: 59px; font-size: 8.4px; line-height: 12px; color: var(--ink); white-space: nowrap; }
  .copy ul { list-style: none; }
  .copy li { padding-left: 16px; position: relative; }
  .copy li::before { content: ""; position: absolute; left: 2px; top: 4.5px; width: 3.5px; height: 3.5px; border-radius: 50%; background: var(--ink); }

  .bar-chart { position: absolute; left: 59px; }
  .bar-row { position: absolute; left: 0; height: 24px; }
  .bar-label { position: absolute; left: 3px; font-size: 7.2px; font-weight: 500; line-height: 24px; color: var(--navy); white-space: nowrap; letter-spacing: -0.1px; }
  .bar { position: absolute; left: 77px; height: 24px; color: var(--white); font-size: 7.6px; line-height: 24px; text-align: right; padding-right: 10px; white-space: nowrap; }
  .bar--agent { background: var(--bar-dark); }
  .bar--board { background: var(--bar-light); }
  .bar-axis { position: absolute; left: 76px; width: 3px; background: var(--navy); }

  .source-note { position: absolute; left: 59px; top: 566px; display: flex; align-items: center; gap: 4px; font-family: "EB Garamond", Georgia, serif; font-style: italic; font-size: 8.5px; color: var(--ink); white-space: nowrap; }

  .quote-band { position: absolute; top: 618px; height: 104px; background: var(--navy); color: var(--white); }
  .page--left .quote-band { left: 0; width: 510px; padding: 41px 61px 0; }
  .page--right .quote-band { left: 0; width: 508px; padding: 30px 59px 0; }
  .quote-band blockquote { font-style: italic; font-size: 8.4px; line-height: 13px; text-transform: uppercase; letter-spacing: 0.2px; }
  .quote-band cite { display: block; margin-top: 12px; font-style: normal; font-size: 7.6px; text-transform: uppercase; }
  .page--right .quote-band cite { margin-top: 10px; }
</style>
</head>
<body>
<main class="spread">

  <section class="page page--left">
    <div class="page-number">4</div>
    <h2 class="page-title">HOW TO QUALIFY A REAL<br>ESTATE PROFESSIONAL</h2>
    <p class="lede">Questions ALL Real Estate sales professionals should be able to answer</p>
    <ul class="question-list">
      <li>How many homes did you sell last year?</li>
      <li>What are you percentage of homes that are selling?</li>
      <li>What is your average list to sales price ratio vs. the average for the market?</li>
      <li>What is your average marketing time vs. the MLS average marketing time?</li>
      <li>Do you have a list of past clients I can call?</li>
      <li>Do you follow up on all showings and will you give me feedback?</li>
      <li>Do you have a copy of the Realtor Code of Ethics?</li>
      <li>How much money do you spend each year on education and sales training?</li>
      <li>Are you full time?</li>
    </ul>
    <aside class="power-thought">
      <h3>POWER THOUGHT</h3>
      <p>Hire the professional who is best qualified to handle your most valuable asset, your home.</p>
    </aside>
    <footer class="quote-band">
      <blockquote>I believe that if you show people the problems and you show them the solutions they will be moved to act.</blockquote>
      <cite>- &nbsp;Elias Marlowe</cite>
    </footer>
  </section>

  <section class="page page--right">
    <div class="page-number">5</div>
    <h2 class="page-title">HOW CAN I HELP YOU?</h2>
    <p class="lede">My goal is to sell your home for the most amount of money, in the shortest period of time. So how do I compare to other Realtors out there…?</p>

    <h3 class="section-band" style="top:172px">AVERAGE DAYS ON THE MARKET</h3>
    <div class="copy" style="top:203px">
      <p>Less days on market means</p>
      <ul>
        <li>Less showings and time away from home.</li>
        <li>Less strangers in your home.</li>
        <li>Less cleaning.</li>
      </ul>
    </div>
    <div class="bar-chart" style="top:274px">
      <div class="bar-axis" style="top:0;height:56px"></div>
      <div class="bar-row" style="top:2px"><span class="bar-label">MARCUS HALLWARD</span><span class="bar bar--agent" style="width:83px">35</span></div>
      <div class="bar-row" style="top:32px"><span class="bar-label">CVREB AVERAGE</span><span class="bar bar--board" style="width:110px">57</span></div>
    </div>

    <h3 class="section-band" style="top:358px">PERCENTAGE OF LIST PRICE ACHIEVED FOR LISTINGS</h3>
    <div class="copy" style="top:387px">
      <p>Multiply 2.89% by your estimated sale price to determine to<br>additional amount that I will negotiate for you.</p>
      <ul>
        <li>2.89 x $200,000= $5,790</li>
        <li>2.89 x $350,000= $7,311</li>
        <li>2.89 x 550,000= $15,895</li>
        <li>2.89 x 750,000= $21,675</li>
      </ul>
    </div>
    <div class="bar-chart" style="top:479px">
      <div class="bar-axis" style="top:0;height:58px"></div>
      <div class="bar-row" style="top:3px"><span class="bar-label">MARCUS HALLWARD</span><span class="bar bar--agent" style="width:150px">99.40%</span></div>
      <div class="bar-row" style="top:33px"><span class="bar-label">CVREB AVERAGE</span><span class="bar bar--board" style="width:110px">96.51%</span></div>
    </div>

    <p class="source-note">
      <svg width="15" height="15" viewBox="0 0 15 15" aria-hidden="true"><g stroke="#1f2647" stroke-width="2.4" stroke-linecap="round"><line x1="7.5" y1="1.5" x2="7.5" y2="13.5"/><line x1="2.3" y1="4.5" x2="12.7" y2="10.5"/><line x1="2.3" y1="10.5" x2="12.7" y2="4.5"/></g></svg>
      Statistics provided by the Cedar Valley Real Estate Board
    </p>

    <footer class="quote-band">
      <blockquote>Remember, if you ever need a helping hand, it’s at the end of your arm, as you get older, remember you have another hand: the first is to help yourself, the second is to help others.</blockquote>
      <cite>- &nbsp;Clara Whitfield</cite>
    </footer>
  </section>

</main>
</body>
</html>
```